Wireless Internet Service Provider website design

We need a Internet Service Provider website that show the packages that we offer as well as the functionality where customers have the option of clicking on the various packages and be linked to a page where they can sign up for our services.
We need about 10-15 pages.
A. Integrated online store.
B. Live chat.
C. Social media page
My old website. Brindleport.nyc

Example: http://quarrylinknet.com/services/residential/ Added Tuesday, June 7, 2016

Target Market(s)

Residential and small businesses

Industry/Entity Type

Internet

Coding

Coded - Design and coding required

Number of Pages Required

5+ page

Font styles to use
Serif
Sans Serif
Script

Colors
3176b5
85cae6
ffffff

Requirements
Must have
• Online store and live chat, drop down details on pricing from current website
Nice to have
• great design, functional website,

```html
<!DOCTYPE html>
<html lang="en">
<head>
<meta charset="utf-8">
<title>Brindleport Wireless</title>
<link href="https://fonts.googleapis.com/css2?family=Michroma&family=Open+Sans:ital,wght@0,400;0,600;0,700;1,400&display=swap" rel="stylesheet">
<style>
:root{
  --blue:#3176b5;
  --blue-dark:#2a67a3;
  --sky:#85cae6;
  --sky-band:#6ccbea;
  --white:#ffffff;
  --ink:#333a40;
  --muted:#666d73;
  --light:#f2f3f5;
  --footer-base:#3a3b3d;
}
*{margin:0;padding:0;box-sizing:border-box}
html,body{width:1200px;height:3010px;overflow:hidden}
body{position:relative;font-family:"Open Sans",Arial,sans-serif;color:var(--ink);background:var(--white)}
.abs{position:absolute}
.display{font-family:"Michroma","Open Sans",sans-serif}

/* header */
.topbar{left:650px;top:0;width:460px;height:36px;background:var(--blue);color:var(--white);font-size:13px;display:flex;align-items:center;justify-content:space-around;border-radius:0 0 6px 6px}
.topbar span{display:flex;align-items:center;gap:8px}
.brand-badge{left:88px;top:0;width:224px;height:200px;background:var(--white);border-radius:0 0 112px 112px;z-index:3;display:flex;flex-direction:column;align-items:center;justify-content:center;gap:10px}
.brand-dot{width:54px;height:54px;border-radius:50%;background:var(--blue)}
.brand-name{font-weight:700;font-size:19px;color:var(--blue)}
.nav{left:390px;top:68px;display:flex;gap:38px;font-size:12px;font-weight:700;color:#3d4248}
.nav a{color:inherit;text-decoration:none;position:relative}
.nav .active{color:var(--blue)}
.nav .active::after{content:"";position:absolute;left:-10px;right:-10px;top:26px;height:3px;background:var(--blue)}
.search{left:1074px;top:60px;width:38px;height:38px;border-radius:50%;background:var(--blue);display:flex;align-items:center;justify-content:center}

/* hero */
.hero{left:0;top:110px;width:1200px;height:532px;background:#050708}
.hero-photo{left:500px;top:110px;width:700px;height:532px;background:radial-gradient(circle at 62% 55%,#d9a37a 0,#8a5a3c 18%,#1c3440 45%,#050708 75%)}
.hero h1{left:86px;top:278px;font-size:38px;color:var(--white);font-weight:400;letter-spacing:2px}
.hero-sub{left:86px;top:338px;font-size:19px;font-weight:700;color:var(--sky);letter-spacing:1px}
.hero-text{left:86px;top:384px;width:540px;font-size:12.5px;line-height:26px;color:var(--white)}
.hero-btn{left:86px;top:488px;width:198px;height:52px;border:2px solid var(--white);border-radius:26px;color:var(--white);font-weight:700;font-size:16px;display:flex;align-items:center;justify-content:center}
.dots{left:88px;top:610px;display:flex;gap:6px}
.dots i{width:14px;height:14px;border-radius:50%;border:2px solid var(--white)}
.dots i.on{background:var(--blue)}

/* shared */
.notch{width:84px;height:84px;border-radius:50%;background:var(--white);display:flex;align-items:center;justify-content:center;left:558px}
.notch i{width:40px;height:40px;border-radius:50%;background:var(--blue)}
.sec-title{left:0;width:1200px;text-align:center;font-size:19px;color:var(--blue);font-weight:400}
.sec-title em{font-style:normal;color:var(--sky)}
.sec-text{left:250px;width:700px;text-align:center;font-size:12px;line-height:30px;color:var(--muted)}

/* welcome */
.service{width:300px;text-align:center}
.service-icon{width:116px;height:116px;border-radius:50%;margin:0 auto;border:5px solid #d7eef8;background:var(--sky);display:flex;align-items:center;justify-content:center}
.service-icon.strong{background:var(--blue);border-color:#c9dbee}
.service h3{margin-top:36px;font-size:15px;font-weight:600;line-height:22px;letter-spacing:1px;color:#3a3e42}
.service p{margin-top:18px;font-size:11.5px;line-height:27px;color:var(--muted)}
.read-btn{margin:20px auto 0;width:122px;height:40px;border-radius:20px;border:2px solid #cde6f3;color:#a8d2ea;font-size:12px;font-weight:700;display:flex;align-items:center;justify-content:center}
.read-btn.strong{border-color:var(--blue);color:var(--blue)}

/* plans */
.plans{left:0;top:1218px;width:1200px;height:672px;background:var(--light)}
.plan{background:var(--white);text-align:center;box-shadow:0 0 4px rgba(0,0,0,.06)}
.plan.featured{box-shadow:0 2px 12px rgba(0,0,0,.22);z-index:2}
.plan-star{width:32px;height:32px;border-radius:50%;background:var(--blue);margin:0 auto;display:flex;align-items:center;justify-content:center;position:relative}
.featured .plan-star{background:var(--sky)}
.plan-rule{position:absolute;left:20px;right:20px;top:50%;height:1px;background:#ddd;z-index:-1}
.plan h4{font-size:15px;font-weight:700;color:#3a3e42;margin-top:14px}
.price{margin-top:12px;height:46px;background:var(--blue);color:var(--white);display:flex;align-items:center;justify-content:center;gap:6px;font-size:24px;font-weight:700}
.featured .price{background:var(--sky)}
.price small{font-size:13px;font-weight:400}
.feat{font-size:12px;color:var(--muted);height:37px;line-height:37px;border-bottom:1px solid #e9e9e9}
.speed{font-size:12px;font-style:italic;color:var(--blue);height:44px;line-height:44px}
.featured .speed{color:var(--sky)}
.plan-btn{margin:14px auto 0;width:120px;height:40px;border-radius:20px;background:var(--blue);color:var(--white);font-size:12px;font-weight:700;display:flex;align-items:center;justify-content:center}
.featured .plan-btn{background:var(--sky)}

/* testimonials */
.testimonials{left:0;top:1890px;width:1200px;height:414px;background:linear-gradient(160deg,#7dd6f1,#62c6e8 60%,#74d0ee)}
.testimonials .sec-title,.testimonials .sec-text{color:var(--white)}
.avatar{width:88px;height:88px;border-radius:50%;border:4px solid var(--white);background:linear-gradient(#4c6a7c,#2c3e4a)}
.quote{width:240px;font-size:10.5px;font-style:italic;line-height:20px;color:var(--white)}
.quote .mark{font-size:26px;font-weight:700;line-height:10px;vertical-align:-8px;margin-right:6px}
.tname{font-size:12px;font-weight:700;color:#245a8a}
.stars{font-size:11px;color:var(--white);letter-spacing:1px}

/* why */
.why{left:0;top:2304px;width:1200px;height:386px;background:linear-gradient(90deg,#eceef0,#f5f6f7)}
.why-photo{left:0;top:2304px;width:400px;height:386px;background:linear-gradient(120deg,#f4f4f4,#d7d2cf 50%,#ece8e6)}
.why h2{left:426px;top:2340px;font-size:26px;font-weight:400;color:var(--blue)}
.why h2 em{font-style:normal;color:var(--sky)}
.why-sub{left:426px;top:2392px;font-size:16px;color:#4a4e52;letter-spacing:1px}
.why-text{left:426px;top:2432px;width:750px;font-size:12px;line-height:30px;color:var(--muted)}
.feature{width:200px;text-align:center;font-size:14px;font-weight:600;color:#3a3e42;line-height:22px}
.feature svg{display:block;margin:0 auto 10px}

/* footer */
.footer{left:0;top:2690px;width:1200px;height:254px;background:var(--blue)}
.footer-brand{left:86px;top:2730px;width:240px;display:flex;flex-direction:column;align-items:center;gap:16px}
.footer-brand i{width:110px;height:110px;border-radius:50%;background:var(--white)}
.footer-brand span{font-weight:700;font-size:24px;color:var(--white)}
.fcol h5{font-size:17px;font-weight:700;color:var(--white);margin-bottom:20px}
.fcol{color:var(--white);font-size:11.5px;line-height:20px}
.citem{display:flex;gap:12px;align-items:flex-start;margin-bottom:8px}
.citem u{text-decoration:underline}
.email-box{margin-top:14px;width:240px;height:34px;background:var(--white);color:#888;font-size:11.5px;padding-left:12px;line-height:34px}
.sub-btn{margin-top:8px;width:82px;height:26px;background:var(--sky);color:var(--white);font-size:11px;display:flex;align-items:center;justify-content:center}
.socials{display:flex;gap:10px;margin-top:18px}
.socials i{width:36px;height:36px;border-radius:50%;border:2px solid var(--white)}
.bottom{left:0;top:2944px;width:1200px;height:66px;background:var(--footer-base);color:var(--white);font-size:12px;display:flex;align-items:center;justify-content:center}

/* live chat */
.livechat{left:1154px;top:904px;width:46px;height:192px;background:var(--sky);border-radius:8px 0 0 8px;display:flex;align-items:center;justify-content:center}
.livechat span{transform:rotate(-90deg);color:var(--white);font-weight:700;font-size:17px;letter-spacing:2px;white-space:nowrap}
</style>
</head>
<body>

<!-- header -->
<div class="abs topbar">
  <span><svg width="14" height="14" viewBox="0 0 24 24" fill="#fff"><path d="M6.6 10.8a15 15 0 006.6 6.6l2.2-2.2c.3-.3.7-.4 1-.2 1.1.4 2.3.6 3.6.6.6 0 1 .4 1 1V20c0 .6-.4 1-1 1A17 17 0 013 4c0-.6.4-1 1-1h3.5c.6 0 1 .4 1 1 0 1.3.2 2.5.6 3.6.1.3 0 .7-.2 1z"/></svg>Call Us : (866) 555-0142</span>
  <span><svg width="15" height="14" viewBox="0 0 24 22" fill="#fff"><path d="M0 1h4l3 12h13l3-9H7" stroke="#fff" stroke-width="2" fill="none"/><circle cx="9" cy="18" r="2"/><circle cx="18" cy="18" r="2"/></svg>Shopping Cart is : (0) Items</span>
</div>
<div class="abs brand-badge"><i class="brand-dot"></i><span class="brand-name">Brindleport Wireless</span></div>
<nav class="abs nav">
  <a class="active">HOME</a><a>WHY BRINDLEPORT</a><a>PLANS &amp; PACKAGES</a><a>MY ACCOUNT</a><a>GALLERY</a><a>CONTACT US</a>
</nav>
<div class="abs search"><svg width="16" height="16" viewBox="0 0 24 24" fill="none" stroke="#fff" stroke-width="3"><circle cx="10" cy="10" r="7"/><path d="M15 15l6 6"/></svg></div>

<!-- hero -->
<section class="abs hero"></section>
<div class="abs hero-photo" role="img" aria-label="Glowing hand holding a large wireless signal symbol against a dark background"></div>
<h1 class="abs display" style="left:86px;top:278px;font-size:36px;color:#fff;font-weight:400;letter-spacing:2px">BRINDLEPORT WIRELESS</h1>
<div class="abs hero-sub">LOCALLY OWN RELIABLE SUPER FAST INTERNET</div>
<p class="abs hero-text">Brindleport has a range of affordable plans that provide New Yorker with the best wireless internet service. Plans provide up to 500 Mbps download speeds, unlimited internet we have plans starting at just $39.99 per month.</p>
<div class="abs hero-btn">ONLINE STORE</div>
<div class="abs dots"><i></i><i></i><i class="on"></i><i></i><i></i></div>

<!-- welcome -->
<div class="abs notch" style="top:600px"><i></i></div>
<h2 class="abs sec-title display" style="top:690px">WELCOME TO <em>BRINDLEPORT WIRELESS</em></h2>
<p class="abs sec-text" style="top:730px">Brindleport has a range of affordable plans that provide New Yorker with the best wireless internet service. Plans provide up to 500 Mbps download speeds, unlimited internet usage per month. In most areas, we have plans starting at just $39.99 per month. For plan deals, pricing and availability of packages in your area enter your address below</p>

<div class="abs service" style="left:98px;top:822px">
  <div class="service-icon"><svg width="44" height="40" viewBox="0 0 24 22" fill="#fff"><path d="M12 1L1 11h3v10h6v-6h4v6h6V11h3z"/></svg></div>
  <h3>RESIDENTIAL<br>INTERNET ACCESS</h3>
  <p>Brindleport has a range of affordable plans that provide New Yorker with the best wireless internet service. Plans provi unlim in your area enter your address below</p>
  <div class="read-btn">READ MORE</div>
</div>
<div class="abs service" style="left:446px;top:822px">
  <div class="service-icon strong"><svg width="44" height="40" viewBox="0 0 24 22" fill="#fff"><path d="M8 4V2h8v2h6v16H2V4zm2 0h4V3h-4z"/><rect x="2" y="10" width="20" height="1.5" fill="#3176b5"/></svg></div>
  <h3>BUSINESS<br>INTERNET ACCESS</h3>
  <p>Brindleport has a range of affordable plans that provide New Yorker with the best wireless internet service. Plans provi unlim in your area enter your address below</p>
  <div class="read-btn strong">READ MORE</div>
</div>
<div class="abs service" style="left:792px;top:822px">
  <div class="service-icon"><svg width="46" height="40" viewBox="0 0 24 20" fill="none" stroke="#fff" stroke-width="2.4" stroke-linecap="round"><path d="M2 7a14 14 0 0120 0M5.5 10.5a9 9 0 0113 0M9 14a4 4 0 016 0"/><circle cx="12" cy="17.5" r="1.4" fill="#fff"/></svg></div>
  <h3>UNLIMITED<br>INTERNET USAGE</h3>
  <p>Brindleport has a range of affordable plans that provide New Yorker with the best wireless internet service. Plans provi unlim in your area enter your address below</p>
  <div class="read-btn">READ MORE</div>
</div>

<!-- plans -->
<section class="abs plans"></section>
<div class="abs notch" style="top:1176px"><i></i></div>
<h2 class="abs sec-title display" style="top:1264px">PLANS <em>&amp; PACKAGES</em></h2>
<p class="abs sec-text" style="top:1300px">Brindleport has a range of affordable plans that provide New Yorker with the best wireless internet service. Plans provide up to 500 Mbps download speeds, pricing and availability of packages in your area enter your address below</p>

<div class="abs plan" style="left:92px;top:1394px;width:278px;height:386px;padding-top:18px">
  <div class="plan-star"><span class="plan-rule"></span><svg width="14" height="14" viewBox="0 0 24 24" fill="#fff"><path d="M12 2l3 7 7 .6-5.3 4.7 1.6 7.2L12 17.8 5.7 21.5l1.6-7.2L2 9.6 9 9z"/></svg></div>
  <h4>BRINDLEPORT SIMPLICITY</h4>
  <div class="price">$39.99 / <small>mo./1yr</small></div>
  <div class="feat">Free smart router</div><div class="feat">Free internet protection</div><div class="feat">Unlimited Brindleport Wi-Fi access</div>
  <div class="speed">5 Mbps Download Speed</div>
  <div class="plan-btn">SIGN UP NOW</div>
</div>
<div class="abs plan" style="left:620px;top:1394px;width:238px;height:386px;padding-top:18px">
  <div class="plan-star"><svg width="14" height="14" viewBox="0 0 24 24" fill="#fff"><path d="M12 2l3 7 7 .6-5.3 4.7 1.6 7.2L12 17.8 5.7 21.5l1.6-7.2L2 9.6 9 9z"/></svg></div>
  <h4>BRINDLEPORT SUPER-PAK</h4>
  <div class="price">$ 69.99 / <small>mo./1yr</small></div>
  <div class="feat">Free smart router</div><div class="feat">Free internet protection</div><div class="feat">Unlimited Brindleport Wi-Fi access</div>
  <div class="speed">25 Mbps Download Speed</div>
  <div class="plan-btn">SIGN UP NOW</div>
</div>
<div class="abs plan" style="left:864px;top:1394px;width:244px;height:386px;padding-top:18px">
  <div class="plan-star"><svg width="14" height="14" viewBox="0 0 24 24" fill="#fff"><path d="M12 2l3 7 7 .6-5.3 4.7 1.6 7.2L12 17.8 5.7 21.5l1.6-7.2L2 9.6 9 9z"/></svg></div>
  <h4>BRINDLEPORT ACTION PAK</h4>
  <div class="price">$89.99 / <small>mo./1yr</small></div>
  <div class="feat">Free smart router</div><div class="feat">Free internet protection</div><div class="feat">Unlimited Brindleport Wi-Fi access</div>
  <div class="speed">50 Mbps Download Speed</div>
  <div class="plan-btn">SIGN UP NOW</div>
</div>
<div class="abs plan featured" style="left:332px;top:1372px;width:282px;height:442px;padding-top:24px">
  <div class="plan-star"><svg width="14" height="14" viewBox="0 0 24 24" fill="#fff"><path d="M12 2l3 7 7 .6-5.3 4.7 1.6 7.2L12 17.8 5.7 21.5l1.6-7.2L2 9.6 9 9z"/></svg></div>
  <h4>BRINDLEPORT VALUE PAK</h4>
  <div class="price">$49.95 / <small>mo./1yr</small></div>
  <div class="feat" style="margin-top:18px">Free smart router</div><div class="feat">Free internet protection</div><div class="feat">Unlimited Brindleport Wi-Fi access</div>
  <div class="speed">10 Mbps Download Speed</div>
  <div class="plan-btn">SIGN UP NOW</div>
</div>

<!-- testimonials -->
<section class="abs testimonials"></section>
<div class="abs notch" style="top:1848px"><i></i></div>
<h2 class="abs sec-title display" style="top:1936px;color:#fff">OUR TESTIMONIALS</h2>
<p class="abs sec-text" style="top:1972px;color:#fff">Brindleport has a range of affordable plans that provide New Yorker with the best wireless internet service. Plans provide up to 500 Mbps download speeds, pricing and availability of packages in your area enter your address below</p>

<div class="abs avatar" style="left:88px;top:2066px" role="img" aria-label="Customer portrait"></div>
<div class="abs quote" style="left:194px;top:2074px"><span class="mark">“</span>Thanks for your great service. I love my internet and your quick response to my questions and concerns. I would definitely refer Brindleport to my friends and family.</div>
<div class="abs tname" style="left:194px;top:2176px">MARA ELLISON</div>
<div class="abs stars" style="left:194px;top:2194px">★★★★★</div>

<div class="abs avatar" style="left:438px;top:2066px" role="img" aria-label="Customer portrait"></div>
<div class="abs quote" style="left:544px;top:2074px"><span class="mark">“</span>By far the best customer service I have ever received from an Internet service provider. Brindleport stands above the rest for the rapid resolution to my problem.</div>
<div class="abs tname" style="left:544px;top:2176px">THEO BRANDT</div>
<div class="abs stars" style="left:544px;top:2194px">★★★★★</div>

<div class="abs avatar" style="left:790px;top:2066px" role="img" aria-label="Customer portrait"></div>
<div class="abs quote" style="left:894px;top:2074px"><span class="mark">“</span>Brindleport is the best internet service provider in Brooklyn, finally a better option to internet service. My family and I are streaming. I'm a satisfied customer.</div>
<div class="abs tname" style="left:894px;top:2176px">NINA CALLOWAY</div>
<div class="abs stars" style="left:894px;top:2194px">★★★★★</div>

<!-- why -->
<section class="abs why"></section>
<div class="abs why-photo" role="img" aria-label="Hand holding a white smartphone showing the company name"></div>
<h2 class="abs display" style="left:426px;top:2340px;font-size:25px;font-weight:400;color:var(--blue)">WHY <span style="color:var(--sky)">BRINDLEPORT</span></h2>
<div class="abs why-sub display">FAST DOWNLOAD &amp; UPLOAD SPEEDS AT AN AFFORDABLE PRICE</div>
<p class="abs why-text">Brindleport has a range of affordable plans that provide New Yorker with the best wireless internet service. Plans provide up to 500 Mbps download speeds, unlimited internet usage per month. In most areas, we have plans starting at just $39.99 per month. For plan deals, pricing and availability of packages in your area enter your address below</p>
<div class="abs feature" style="left:396px;top:2544px">
  <svg width="44" height="40" viewBox="0 0 26 22" fill="#6cbde0"><path d="M2 2h14v9H7l-4 3v-3H2z"/><path d="M18 6h6v9h-1v3l-4-3h-8v-2h7z"/></svg>CUSTOMER<br>SUPPORT CENTER</div>
<div class="abs feature" style="left:618px;top:2544px">
  <svg width="44" height="40" viewBox="0 0 26 22" fill="none" stroke="#6cbde0" stroke-width="2.4"><circle cx="9" cy="13" r="4"/><circle cx="9" cy="13" r="7" stroke-dasharray="2.5 2"/><circle cx="20" cy="6" r="2.5"/><circle cx="20" cy="6" r="4.5" stroke-dasharray="2 1.6"/></svg>EQUIPMENT<br>OPTIONS</div>
<div class="abs feature" style="left:808px;top:2544px">
  <svg width="44" height="40" viewBox="0 0 24 22" fill="#6cbde0"><path d="M12 1l3.2 7 7.6.7-5.8 5 1.8 7.4L12 17.2l-6.8 3.9L7 13.7l-5.8-5 7.6-.7z"/></svg>CUSTOMER<br>GUARANTEE</div>

<!-- footer -->
<footer class="abs footer"></footer>
<div class="abs footer-brand"><i></i><span>Brindleport Wireless</span></div>
<div class="abs fcol" style="left:390px;top:2738px;width:200px">
  <h5>CONTACT US</h5>
  <div class="citem"><svg width="14" height="14" viewBox="0 0 24 24" fill="#fff"><path d="M6.6 10.8a15 15 0 006.6 6.6l2.2-2.2c.3-.3.7-.4 1-.2 1.1.4 2.3.6 3.6.6.6 0 1 .4 1 1V20c0 .6-.4 1-1 1A17 17 0 013 4c0-.6.4-1 1-1h3.5c.6 0 1 .4 1 1 0 1.3.2 2.5.6 3.6.1.3 0 .7-.2 1z"/></svg>866-555-0142 (Phone)</div>
  <div class="citem"><svg width="14" height="14" viewBox="0 0 24 24" fill="#fff"><rect x="6" y="2" width="12" height="6"/><rect x="2" y="9" width="20" height="9" rx="2"/><rect x="6" y="15" width="12" height="7"/></svg>718-555-0177 (Fax)</div>
  <div class="citem"><svg width="14" height="14" viewBox="0 0 24 24" fill="#fff"><path d="M2 5h20v14H2z"/><path d="M2 5l10 8 10-8" stroke="#3176b5" stroke-width="2" fill="none"/></svg><u>support@brindleport.nyc</u></div>
  <div class="citem"><svg width="14" height="14" viewBox="0 0 24 24" fill="#fff"><path d="M12 1a8 8 0 00-8 8c0 6 8 14 8 14s8-8 8-14a8 8 0 00-8-8zm0 11a3 3 0 110-6 3 3 0 010 6z"/></svg><span>P.O Box 40117 &nbsp; Brooklyn<br>NY 11201</span></div>
</div>
<div class="abs fcol" style="left:624px;top:2738px;width:250px">
  <h5>NEWSLETTER</h5>
  <div>Register Your email address to get information about us</div>
  <div class="email-box">Email Address</div>
  <div class="sub-btn">SUBSCRIBE</div>
</div>
<div class="abs fcol" style="left:904px;top:2738px;width:210px">
  <h5>FOLLOW US</h5>
  <div>Lorem ipsum dolor sit amet, conse ctetur adipiscing elit. Nulla in purus nibh. Donec ornare.</div>
  <div class="socials"><i></i><i></i><i></i><i></i><i></i></div>
</div>
<div class="abs bottom">© Copyright 2016 Brindleport Wireless All Rights Reserved</div>

<!-- live chat -->
<div class="abs livechat"><span>LIVECHAT</span></div>

</body>
</html>
```